Price Trend Graphic for Estimates

I want to add a graphic to my estimates that shows the projected price trend of the work we are quoting to the customer. I have attached a couple ideas I was working on but they are garbage. Hopefully you can see the intent and make it look a lot better. Basically I want the customer to see a really a professional / technological graphic that will stimulate them to purchase Right Now! before the price goes up further. So maybe if the "Today's Price" looks nice and friendly and then becomes more critical and ominous as it goes forward 30 days.... 90 days.... Idea is to psychologically

Target Market(s)

Customers for our Construction business

Industry/Entity Type

Construction

Colors
0054AA
0677BA
7BADD7
CADEEF
E8F1F8
0094D4
00A9DD
6FCCEA
C7EBF8
E9F6FB
FFF300
FFF600
FEFA6F
FFFEC7
FFFEE8
F0912C
F2A743
F7CA91
FBE8D2
FDF5EE

Requirements
Must have
• nice looking graphic with upwards moving arrow and 3 price points
Nice to have
• technological / modern looking chart

```html
<!DOCTYPE html>
<html lang="en">
<head>
<meta charset="UTF-8">
<title>Estimated Price Trend</title>
<link href="https://fonts.googleapis.com/css2?family=Montserrat:wght@300;400;800;900&display=swap" rel="stylesheet">
<style>
  :root {
    --night: #00101e;
    --sky: #7badd7;
    --ocean: #1b75bb;
    --deep: #16588e;
    --signal: #fff300;
    --white: #ffffff;
    --grid: #6d7278;
  }
  * { margin: 0; padding: 0; box-sizing: border-box; }
  html, body {
    width: 1200px;
    height: 849px;
    overflow: hidden;
    background: var(--night);
  }
  .canvas {
    position: relative;
    width: 1200px;
    height: 849px;
    background: var(--night);
    font-family: "Montserrat", sans-serif;
  }
  .title-kicker {
    position: absolute;
    left: 96px;
    top: 54px;
    font-weight: 300;
    font-size: 25px;
    letter-spacing: 5.2px;
    color: var(--sky);
    line-height: 1;
  }
  .title-pill {
    position: absolute;
    left: 70px;
    top: 82px;
    width: 328px;
    height: 37px;
    display: flex;
  }
  .title-pill__label {
    width: 218px;
    height: 100%;
    border: 1.5px solid var(--white);
    border-right-width: 1.5px;
    border-radius: 19px 0 0 19px;
    display: flex;
    align-items: center;
    padding-left: 25px;
    font-weight: 900;
    font-size: 24.5px;
    color: var(--sky);
    letter-spacing: 0.2px;
  }
  .title-pill__bar {
    flex: 1;
    height: 100%;
    background: var(--sky);
    border-radius: 0 19px 19px 0;
  }
  .chart {
    position: absolute;
    left: 0;
    top: 0;
  }
  .chart__grid line { stroke: var(--grid); stroke-width: 1.2; }
  .chart__trend { fill: none; stroke: var(--sky); stroke-width: 6; stroke-linejoin: round; }
  .chart__node { fill: var(--night); stroke: var(--sky); stroke-width: 7; }
  .marker__ring { fill: none; stroke: var(--signal); stroke-width: 2.4; }
  .marker__face { fill: var(--white); }
  .marker__price { font-family: "Montserrat", sans-serif; font-weight: 800; font-size: 27px; text-anchor: middle; }
  .marker__caption { font-family: "Montserrat", sans-serif; font-weight: 400; font-size: 13.5px; text-anchor: middle; letter-spacing: 0.3px; }
  .marker--today { color: var(--sky); }
  .marker--month { color: var(--ocean); }
  .marker--quarter { color: var(--deep); }
  .marker__pin { fill: currentColor; }
  .marker__price, .marker__caption { fill: currentColor; }
</style>
</head>
<body>
<div class="canvas">
  <div class="title-kicker">ESTIMATED</div>
  <div class="title-pill">
    <div class="title-pill__label">PRICE TREND</div>
    <div class="title-pill__bar"></div>
  </div>

  <svg class="chart" width="1200" height="849" viewBox="0 0 1200 849" aria-label="Price trend chart rising from today to 90 days">
    <defs>
      <linearGradient id="area-fill" x1="0" y1="230" x2="0" y2="750" gradientUnits="userSpaceOnUse">
        <stop offset="0" stop-color="#b8651e"/>
        <stop offset="0.2" stop-color="#b78f2a"/>
        <stop offset="0.42" stop-color="#b89b29"/>
        <stop offset="0.62" stop-color="#6b6626"/>
        <stop offset="0.85" stop-color="#222a1f"/>
        <stop offset="1" stop-color="#00101e"/>
      </linearGradient>
    </defs>

    <polygon class="chart__area" fill="url(#area-fill)"
      points="222,566 486,528 750,453 1014,230 1014,750 222,750"/>

    <g class="chart__grid" opacity="0.8">
      <line x1="222" y1="201" x2="1014" y2="201"/>
      <line x1="222" y1="257" x2="1014" y2="257"/>
      <line x1="222" y1="313" x2="1014" y2="313"/>
      <line x1="222" y1="368" x2="1014" y2="368"/>
      <line x1="222" y1="424" x2="1014" y2="424"/>
      <line x1="222" y1="480" x2="1014" y2="480"/>
      <line x1="222" y1="536" x2="1014" y2="536"/>
      <line x1="222" y1="592" x2="1014" y2="592"/>
      <line x1="222" y1="648" x2="1014" y2="648"/>
      <line x1="222" y1="704" x2="1014" y2="704"/>
      <line x1="222" y1="173" x2="222" y2="750"/>
      <line x1="486" y1="173" x2="486" y2="750"/>
      <line x1="750" y1="173" x2="750" y2="750"/>
      <line x1="1014" y1="173" x2="1014" y2="750"/>
    </g>

    <polyline class="chart__trend" points="222,566 486,528 750,453 1036,212"/>
    <polygon class="chart__arrowhead" fill="var(--sky)" points="1023,197 1050,195 1040,221"/>

    <circle class="chart__node" cx="222" cy="566" r="16"/>
    <circle class="chart__node" cx="486" cy="528" r="16"/>
    <circle class="chart__node" cx="750" cy="453" r="16"/>

    <g class="marker marker--today" transform="translate(222 349)">
      <path class="marker__pin" d="M0,167 C-30,127 -88,45 -88,0 A88,88 0 1 1 88,0 C88,45 30,127 0,167 Z"/>
      <circle class="marker__ring" r="76"/>
      <circle class="marker__face" r="66"/>
      <text class="marker__price" y="9">$6,500</text>
      <text class="marker__caption" y="27">Today price</text>
    </g>

    <g class="marker marker--month" transform="translate(486 314)">
      <path class="marker__pin" d="M0,167 C-30,127 -88,45 -88,0 A88,88 0 1 1 88,0 C88,45 30,127 0,167 Z"/>
      <circle class="marker__ring" r="76"/>
      <circle class="marker__face" r="66"/>
      <text class="marker__price" y="9">$7,280</text>
      <text class="marker__caption" y="27">30 Days Price</text>
    </g>

    <g class="marker marker--quarter" transform="translate(750 232)">
      <path class="marker__pin" d="M0,167 C-30,127 -88,45 -88,0 A88,88 0 1 1 88,0 C88,45 30,127 0,167 Z"/>
      <circle class="marker__ring" r="76"/>
      <circle class="marker__face" r="66"/>
      <text class="marker__price" y="9">$7,460</text>
      <text class="marker__caption" y="27">90 Days Price</text>
    </g>
  </svg>
</div>
</body>
</html>
```